Swimming Pool Supply Company Business Cards

We need business cards designed for company. These need to be easy to edit so that we can fill in names, titles, and contact info for each person who works here.

Dalton R. Whitfield
Manager of Legal & Finance
K.L. Brisbane, Incorporated

4837 Grenway Avenue
Marlow Heights, PA 19243

E. dalton@klbrisbane-example.com
M. (215) 555-0173
O. (215) 555-0148

Contact Information for Business Card

Looking to upgrade current business cards with graphic that can be edited. Looking for fresh ideas for an age old industry.

Font styles to use
Serif
Sans Serif

Colors

Designer to choose colors to be used in the design.

Requirements
Must have
• Professional, fresh, unique but professional

```html
<!DOCTYPE html>
<html lang="en">
<head>
<meta charset="utf-8">
<title>Business Cards</title>
<link rel="stylesheet" href="https://fonts.googleapis.com/css2?family=Arimo:wght@400;700&display=swap">
<style>
  :root {
    --backdrop: #2b2b2d;
    --card-white: #ffffff;
    --brand-blue: #1f5fae;
    --navy-deep: #0c0f2b;
    --navy-mid: #1b2e5c;
    --ink-light: #ffffff;
    --icon-ink: #1a2347;
  }
  * { box-sizing: border-box; margin: 0; padding: 0; }
  html, body {
    width: 1200px; height: 1200px; overflow: hidden;
    background: var(--backdrop);
    font-family: "Arimo", Arial, sans-serif;
  }
  .sheet {
    width: 1200px; height: 1200px;
    display: flex; flex-direction: column; align-items: center; justify-content: center;
    gap: 60px;
  }
  .card {
    width: 840px; height: 480px; position: relative;
    box-shadow: 0 18px 40px rgba(0,0,0,0.45);
  }
  .card-front {
    background: var(--card-white);
    display: flex; flex-direction: column; align-items: center; justify-content: center;
  }
  .brand-name {
    color: var(--brand-blue);
    font-weight: 700; font-size: 128px; letter-spacing: 4px; line-height: 1;
  }
  .brand-tagline {
    margin-top: 22px;
    color: var(--brand-blue);
    font-weight: 700; font-size: 24px; letter-spacing: 3px;
  }
  .card-back {
    background: radial-gradient(ellipse at 55% 55%, var(--navy-mid) 0%, #15224a 45%, var(--navy-deep) 100%);
    color: var(--ink-light);
  }
  .person {
    position: absolute; left: 60px; top: 250px; width: 340px;
    text-align: center;
  }
  .person-name { font-size: 32px; line-height: 1.2; }
  .person-title, .person-company { font-size: 23px; line-height: 1.3; }
  .contacts {
    position: absolute; left: 440px; top: 120px;
    display: flex; flex-direction: column; gap: 44px;
  }
  .contact-row { display: flex; align-items: flex-start; gap: 26px; }
  .contact-icon { width: 46px; height: 46px; flex: none; }
  .contact-text { font-size: 23px; line-height: 1.35; padding-top: 4px; }
  .contact-text.phones { line-height: 1.9; padding-top: 0; }
</style>
</head>
<body>
<main class="sheet">
  <section class="card card-front">
    <div class="brand-name">BRISBANE</div>
    <div class="brand-tagline">SWIMMING POOLS, SUPPLIES &amp; ACCESSORIES</div>
  </section>

  <section class="card card-back">
    <div class="person">
      <div class="person-name">Dalton R. Whitfield</div>
      <div class="person-title">Manager of Legal &amp; Finance</div>
      <div class="person-company">K.L. Brisbane, Incorporated</div>
    </div>

    <div class="contacts">
      <div class="contact-row">
        <svg class="contact-icon" viewBox="0 0 46 46" aria-hidden="true">
          <polygon points="23,2 42,12.5 42,33.5 23,44 4,33.5 4,12.5" fill="#fff"/>
          <path d="M13 23 L23 14 L33 23 M16 21 V31 H30 V21" fill="none" stroke="var(--icon-ink)" stroke-width="2.6" stroke-linejoin="round"/>
        </svg>
        <div class="contact-text">4837 Grenway Avenue<br>Marlow Heights, PA 19243</div>
      </div>
      <div class="contact-row">
        <svg class="contact-icon" viewBox="0 0 46 46" aria-hidden="true">
          <polygon points="23,2 42,12.5 42,33.5 23,44 4,33.5 4,12.5" fill="#fff"/>
          <rect x="13" y="16" width="20" height="14" fill="none" stroke="var(--icon-ink)" stroke-width="2"/>
          <path d="M13 16 L23 24 L33 16" fill="none" stroke="var(--icon-ink)" stroke-width="2"/>
        </svg>
        <div class="contact-text">dalton@klbrisbane-example.com</div>
      </div>
      <div class="contact-row">
        <svg class="contact-icon" viewBox="0 0 46 46" aria-hidden="true">
          <polygon points="23,2 42,12.5 42,33.5 23,44 4,33.5 4,12.5" fill="#fff"/>
          <path d="M16 13 l4 -1 l3 6 l-3 2 q2 5 6 7 l2 -3 l6 3 l-1 4 q-2 2 -5 1 q-10 -4 -13 -13 q-1 -4 1 -6 z" fill="var(--icon-ink)"/>
        </svg>
        <div class="contact-text phones">(215) 555-0173<br>(215) 555-0148</div>
      </div>
    </div>
  </section>
</main>
</body>
</html>
```